Bootstrap Website for Sports Technology Company

Create Bootstrap compatible, HTML and CSS stylesheet-based design templates for typography, forms, buttons, charts, navigation and other interface components for the www.lumacrest-hub.com website. All designs should be Responsive CSS and Fluid.
We are transitioning www.lumacrest-hub.com from Wordpress to Bootstrap and are looking for a fresh, clean landing page with navigation to other page styles. Official Colors and font are attached. Designer may recommend button styles, menu navigation, header, footer, etc. Please incorporate the graphic elements found on the lumacrest-hub.com website.
Page Styles required:
- Landing Page
- Secondary Landing Page
- Five different Page Styles
- small, medium and large buttons
Designers are encouraged to submit the landing page with navigation. We will comment quickly to help with finalizing the design for final selection.
Industry/Entity Type
It Company
Look and feel
Each slider illustrates characteristics of the customer's brand and the style your logo design should communicate.

```html
<!DOCTYPE html>
<html lang="en">
<head>
<meta charset="utf-8">
<title>Lumacrest — Sign Up</title>
<link rel="stylesheet" href="https://fonts.googleapis.com/css2?family=Mulish:wght@400;600;800&display=swap">
<style>
:root{
  --blue:#3a62b8;
  --ink:#474747;
  --grey-word:#7a7a7a;
  --field-border:#8a8a8a;
  --hero-light:#f1f1f1;
  --hero-mid:#dedede;
  --header-bg:#f4f4f4;
  --footer-bg:#c3c3c3;
  --btn-top:#6a6a6a;
  --btn-bottom:#0e0e0e;
  --white:#ffffff;
  --art:#d4d4d4;
}
*{box-sizing:border-box;margin:0;padding:0}
html,body{width:1200px;height:1088px;overflow:hidden;background:var(--white);font-family:"Mulish",sans-serif}
.page{position:relative;width:1200px;height:1088px}
.abs{position:absolute}

.site-header{left:0;top:0;width:1200px;height:110px;background:linear-gradient(#fbfbfb,var(--header-bg));border-bottom:1px solid #d0d0d0}
.brand{left:204px;top:36px;display:flex;align-items:center;gap:10px;color:var(--blue);font-size:28px;font-weight:600}
.brand-dot{width:30px;height:30px;border-radius:50%;background:#6b6b6b}
.main-nav{right:200px;top:18px;display:flex;gap:8px}
.main-nav a{display:block;height:27px;line-height:25px;border:1px solid #c8c8c8;background:linear-gradient(#fff,#ececec);color:var(--blue);text-decoration:none;font-size:14px;font-weight:600;text-align:center;letter-spacing:.5px}

.hero{left:0;top:110px;width:1200px;height:595px;background:radial-gradient(ellipse at 58% 35%,var(--hero-light),var(--hero-mid) 80%)}
.art{background:var(--art);border-radius:4px}
.pill{display:block;width:159px;height:32px;border-radius:3px;background:linear-gradient(var(--btn-top),var(--btn-bottom) 55%,#2a2a2a);color:var(--white);font-size:22px;text-align:center;line-height:32px;letter-spacing:.5px;box-shadow:0 1px 2px rgba(0,0,0,.4)}

.signup-title{left:523px;font-size:34px;color:var(--ink);font-weight:600}
.field{height:29px;border:1px solid var(--field-border);border-radius:3px;background:var(--white);padding-left:10px;font-size:17px;color:#a8a8a8;line-height:27px}
.terms{left:529px;width:400px;font-size:8px;line-height:11px;color:var(--ink)}

.share{height:26px;border:1px solid #cfcfcf;background:linear-gradient(#fff,#f0f0f0);display:flex;align-items:center;gap:10px;padding-left:10px;font-size:12px;color:var(--blue)}
.share .mark{width:12px;height:12px;background:var(--blue);border-radius:2px}
.share .mark.round{border-radius:50%}
.share.mail{color:var(--ink)}

.wordmark{left:422px;top:488px;width:576px;height:90px;display:flex;align-items:center;justify-content:space-between;font-size:62px;letter-spacing:-1px;white-space:nowrap}
.wordmark-name{color:var(--blue);font-weight:600}
.wordmark-product{color:var(--grey-word);font-weight:600}
.wordmark-figure{width:42px;height:86px;background:#cfcfcf;border-radius:4px}

.beta{left:438px;top:797px;font-size:44px;font-weight:800;color:var(--ink);text-shadow:0 2px 2px rgba(0,0,0,.25)}

.footer-rule{left:0;top:930px;width:1200px;height:4px;background:var(--blue)}
.site-footer{left:0;top:934px;width:1200px;height:154px;background:linear-gradient(135deg,#cbcbcb,var(--footer-bg))}
.footer-col h4{font-size:13.6px;font-weight:600;color:var(--blue);margin-bottom:10px}
.footer-col ul{list-style:none;padding-left:10px}
.footer-col li{font-size:10px;line-height:12.4px;color:var(--white)}
.copyright{left:201px;top:1047px;font-size:8px;color:var(--white)}
</style>
</head>
<body>
<div class="page">

  <header class="site-header abs">
    <div class="brand abs"><span class="brand-dot"></span>Lumacrest</div>
    <nav class="main-nav abs">
      <a href="#" style="width:91px">WORLD</a>
      <a href="#" style="width:90px">GOLF</a>
      <a href="#" style="width:112px">CLUBHOUSE</a>
    </nav>
  </header>

  <section class="hero abs">
    <div class="art abs" role="img" aria-label="Silhouette of a golfer addressing the ball" style="left:265px;top:45px;width:75px;height:117px"></div>
    <span class="pill abs" style="left:214px;top:176px">COLLECT</span>

    <div class="art abs" role="img" aria-label="Circular arrows analysis icon" style="left:250px;top:248px;width:86px;height:88px;border-radius:50%"></div>
    <span class="pill abs" style="left:214px;top:360px">ANALYZE</span>

    <div class="art abs" role="img" aria-label="Sensor device sending a wireless signal" style="left:244px;top:416px;width:101px;height:88px"></div>
    <span class="pill abs" style="left:214px;top:528px">INSTRUCT</span>

    <h1 class="signup-title abs" style="top:48px">Sign Up</h1>
    <form>
      <div class="field abs" style="left:520px;top:96px;width:200px">First Name</div>
      <div class="field abs" style="left:728px;top:96px;width:201px">Last Name</div>
      <div class="field abs" style="left:520px;top:132px;width:409px">Your Email</div>
      <div class="field abs" style="left:520px;top:169px;width:409px">Re-Enter Email</div>
      <div class="field abs" style="left:520px;top:207px;width:409px">Password</div>
      <p class="terms abs" style="top:248px">Lorem ipsum dolor sit amet, consectetuer adipiscing elit, sed diam nonummy nibh euismod tincidunt ut laoreet dolore magna aliquam erat volutpat.</p>
      <span class="pill abs" style="left:769px;top:304px;width:160px">Sign Up</span>
    </form>

    <div class="share abs" style="left:597px;top:442px;width:90px"><span class="mark"></span>Share</div>
    <div class="share abs" style="left:702px;top:441px;width:90px"><span class="mark round"></span>Post</div>
    <div class="share abs" style="left:807px;top:441px;width:90px"><span class="mark"></span>Share</div>
    <div class="share mail abs" style="left:909px;top:441px;width:90px">
      <svg width="26" height="16" viewBox="0 0 26 16"><rect x="1" y="1" width="24" height="14" fill="none" stroke="#555" stroke-width="1.4"/><path d="M1 1 L13 10 L25 1" fill="none" stroke="#555" stroke-width="1.4"/></svg>Email</div>

    <div class="wordmark abs">
      <span class="wordmark-name">Lumacrest</span>
      <span class="wordmark-figure" role="img" aria-label="Small golfer silhouette"></span>
      <span class="wordmark-product">Collect</span>
    </div>
  </section>

  <div class="art abs" role="img" aria-label="Line drawing of a golfer mid-swing beside a golf bag with sensors" style="left:204px;top:725px;width:158px;height:187px;background:#efefef"></div>
  <h2 class="beta abs">Now in Private Beta!</h2>

  <div class="footer-rule abs"></div>
  <footer class="site-footer abs">
    <div class="footer-col abs" style="left:198px;top:18px">
      <h4>Lumacrest Portal</h4>
      <ul><li>Team Portal</li><li>Lumacrest Exchange</li></ul>
    </div>
    <div class="footer-col abs" style="left:379px;top:17px">
      <h4>Who We Are</h4>
      <ul><li>About us</li><li>Our Company</li><li>Product Development</li></ul>
    </div>
    <div class="footer-col abs" style="left:570px;top:18px">
      <h4>Outreach</h4>
      <ul>
        <li>Lumacrest Attends Harvest Grill Brightpath 2013</li>
        <li>Lumacrest Attends Ridgeline Venture Summit 2013</li>
        <li>Ready to Tee Up First of Three Product Launches</li>
        <li>Lumacrest Attends TechPulse Spring 2013</li>
      </ul>
    </div>
    <div class="footer-col abs" style="left:886px;top:18px">
      <h4>Other Information</h4>
      <ul><li>Privacy Policy</li><li>Terms &amp; Conditions</li></ul>
    </div>
  </footer>
  <p class="copyright abs">© 2013 All Rights Reserved - Lumacrest Enterprise, LLC.</p>

</div>
</body>
</html>
```